Agriculture new feeding concept for bull fattening needs a one-page flyer *

We are the innovation leader in the field of cattle feeding in Switzerland. Now we are launching a new “Velmasta” project for cattle fatteners, Munimäster (bull fattening). Velmasta is a complete fattening regime (feed, feed additives, services and advice).
Our sales representatives are with customers every day. You advertise the new project with the aim that our internal specialists get an appointment with the customer for a non-binding presentation of the project. This flyer is intended for this purpose.
Effect:
1. Innovative, modern
2. New
3. emotions
4. technical, scientific

You are also welcome to create a “logo” for Velmasta or choose / design your own lettering.
If you wish to use them, you will also find pictures of such fattening bulls in the appendix. However, pictures are not absolutely necessary.
Size A5, one-sided
Title: VELMASTA - for beef fattening professionals
Text:
• Best fattening results
• Top customer service
• Innovative products
• Attractive conditions

Banner or similar:
May we introduce ourselves? or we would be happy to visit you. Etc.

```html
<!DOCTYPE html>
<html lang="en">
<head>
<meta charset="utf-8">
<title>Velmasta – For Beef Fattening Professionals</title>
<link href="https://fonts.googleapis.com/css2?family=Montserrat:wght@600;700;800&display=swap" rel="stylesheet">
<style>
  :root {
    --teal: #1e4a55;
    --teal-deep: #163b45;
    --yellow: #f3c418;
    --orange: #f28a1e;
    --white: #ffffff;
  }
  * { margin: 0; padding: 0; box-sizing: border-box; }
  html, body { width: 847px; height: 1200px; overflow: hidden; background: #eee; }
  .flyer {
    position: relative; width: 847px; height: 1200px; overflow: hidden;
    background: var(--teal);
    font-family: "Montserrat", Arial, sans-serif; color: var(--white);
  }
  .hero-photo {
    position: absolute; left: 0; top: 0; width: 847px; height: 560px;
    background: linear-gradient(180deg, #b9a27a 0%, #d8c27a 40%, var(--yellow) 78%, var(--yellow) 100%);
  }
  .wave { position: absolute; left: 0; top: 440px; width: 847px; height: 200px; }
  .lower-photo {
    position: absolute; left: 0; top: 860px; width: 847px; height: 340px;
    background: linear-gradient(180deg, rgba(30,74,85,0) 0%, rgba(120,130,125,.25) 60%, rgba(150,150,140,.3) 100%);
  }
  .brand {
    position: absolute; top: 200px; width: 100%; text-align: center;
    font-weight: 800; font-size: 116px; letter-spacing: -2px; line-height: 1;
  }
  .tagline {
    position: absolute; top: 338px; left: 50%; transform: translateX(-50%);
    border: 4px solid var(--white); padding: 16px 24px;
    font-weight: 700; font-size: 30px; line-height: 1; white-space: nowrap;
  }
  .brand-echo {
    position: absolute; top: 515px; left: -40px;
    font-weight: 800; font-size: 240px; letter-spacing: -6px; line-height: 1;
    color: var(--orange); white-space: nowrap;
  }
  .photo-circle {
    position: absolute; top: 442px; width: 224px; height: 224px; border-radius: 50%;
    border: 7px solid var(--white);
    background: radial-gradient(circle at 50% 45%, #c8c2b5 0%, #8d8779 60%, #5d5a52 100%);
  }
  .photo-circle.left { left: 182px; }
  .photo-circle.right { left: 420px; background: radial-gradient(circle at 50% 55%, #d7c7ab 0%, #9f7f5c 60%, #5a4634 100%); }
  .benefits { position: absolute; top: 810px; left: 180px; list-style: none; }
  .benefits li {
    display: flex; align-items: center; gap: 22px;
    font-weight: 700; font-size: 41px; line-height: 1; margin-bottom: 17px;
  }
  .benefits svg { width: 34px; height: 34px; flex: none; }
  .contact { position: absolute; top: 1058px; width: 100%; text-align: center; }
  .contact-lead { font-weight: 700; font-size: 24px; }
  .contact-details { margin-top: 12px; font-weight: 700; font-size: 27px; color: var(--orange); }
</style>
</head>
<body>
<div class="flyer">
  <div class="hero-photo" role="img" aria-label="Photo of fattening bulls at a feeding rail, warm yellow tint"></div>
  <svg class="wave" viewBox="0 0 847 200" preserveAspectRatio="none" aria-hidden="true">
    <path d="M0 70 Q423 -10 847 70 L847 200 L0 200 Z" fill="var(--teal)"/>
  </svg>
  <div class="lower-photo" role="img" aria-label="Faint photo of bulls in the barn"></div>

  <div class="brand">Velmasta</div>
  <div class="tagline">For Beef Fattening Professional</div>

  <div class="brand-echo" aria-hidden="true">Velmasta</div>
  <div class="photo-circle left" role="img" aria-label="Photo of bulls resting in a modern barn"></div>
  <div class="photo-circle right" role="img" aria-label="Photo of bulls feeding at the trough"></div>

  <ul class="benefits">
    <li><svg viewBox="0 0 24 24"><path d="M3 13 L9 19 L21 5" fill="none" stroke="var(--orange)" stroke-width="4.5" stroke-linecap="round" stroke-linejoin="round"/></svg>Best fattening results</li>
    <li><svg viewBox="0 0 24 24"><path d="M3 13 L9 19 L21 5" fill="none" stroke="var(--orange)" stroke-width="4.5" stroke-linecap="round" stroke-linejoin="round"/></svg>Top customer service</li>
    <li><svg viewBox="0 0 24 24"><path d="M3 13 L9 19 L21 5" fill="none" stroke="var(--orange)" stroke-width="4.5" stroke-linecap="round" stroke-linejoin="round"/></svg>Innovative products</li>
    <li><svg viewBox="0 0 24 24"><path d="M3 13 L9 19 L21 5" fill="none" stroke="var(--orange)" stroke-width="4.5" stroke-linecap="round" stroke-linejoin="round"/></svg>Attractive conditions</li>
  </ul>

  <div class="contact">
    <p class="contact-lead">Please contact us for more information:</p>
    <p class="contact-details">(09) 5550 4821 - hello@velmasta-feed.ch</p>
  </div>
</div>
</body>
</html>
```